依頼詳細
1.渡航先の選択ページのデザイン
2.出発日の選択ページのデザイン
3.滞在期間の選択ページのデザイン
4.渡航目的の選択ページのデザイン
5.予約方法の選択ページのデザイン

流れが明確であれば、全て繋がった1ページ構成でも結構です

詳しくは添付資料を参照願います
ページ数
5ページ
希望イメージ
シンプル 複雑
単色 カラフル
暗い 明るい
日常 高級
遊び心 厳粛
未来的 伝統的
女性的 男性的
希望する色
青系、濃紺を主にした色合いでお願いいたします
納品ファイル
• 高解像度JPG (.jpg)
補足説明
スクリーンショットおよび、
サイトを構成するファイル一式をご納品いただきます
提案者制限を付加させいただきました
ファイル一式についての補足ですが、AIやPSD等の
画像を作成したツールでの保存形式ファイルもご納品のほどよろしくお願いいたします。
■ 選んだ理由

レベルの高いご提案を頂き、選定に悩みましたが、
「目指すコンセプトとの一致」と作り込み、質問を頂だいた事を鑑みて、選定とさせて頂きました。

■ 提案者全員のお礼・コメント

大変多くのご提案を頂き、どのデザインも甲乙付けがたいご提案で選定に悩みました。
今後また別の機会に、お力添えを頂ければ幸いです。
この度は誠にご提案ありがとうございました。

```html
<!DOCTYPE html>
<html lang="ja">
<head>
<meta charset="utf-8">
<title>海外渡航前ワクチン接種予約サイト</title>
<link rel="stylesheet" href="https://fonts.googleapis.com/css2?family=Noto+Serif+JP:wght@400;500;700&family=Noto+Sans+JP:wght@400;500;700&display=swap">
<style>
  :root{
    --navy:#17186b;
    --navy-deep:#0f1050;
    --footer-blue:#3a3a9c;
    --ink:#222;
    --tag:#f26a6a;
    --btn:#cfcfcf;
    --btn-border:#8a8a8a;
    --line:#777;
    --white:#fff;
  }
  *{margin:0;padding:0;box-sizing:border-box}
  html,body{width:1200px;height:4720px;overflow:hidden;background:var(--white)}
  body{position:relative;font-family:"Noto Serif JP",serif;color:var(--ink)}
  .abs{position:absolute}

  .site-header{left:0;top:0;width:1200px;height:176px;background:var(--navy)}
  .site-title{left:16px;top:18px;color:var(--white);font-size:52px;line-height:68px;font-weight:500}
  .menu-btn{right:0;top:0;width:128px;height:176px;background:var(--navy-deep);display:flex;flex-direction:column;align-items:center;justify-content:center;gap:14px}
  .menu-btn span.bar{display:block;width:64px;height:8px;background:var(--white)}
  .menu-btn .label{color:var(--white);font-family:"Noto Sans JP",sans-serif;font-weight:700;font-size:26px;margin-top:4px}

  .step-bar{left:0;top:176px;width:1200px;height:56px;background:var(--white);border-bottom:4px solid var(--navy)}
  .step-bar p{position:absolute;left:40px;top:4px;font-size:38px;font-weight:700;color:var(--navy)}

  .hero{left:0;top:232px;width:1200px;height:1090px;background:linear-gradient(120deg,#2c2c33 0%,#55555e 35%,#9aa2ad 65%,#d9dde2 100%)}
  .hero-copy{left:60px;top:1020px;color:var(--white);font-size:84px;line-height:100px;font-weight:400;letter-spacing:-1px}

  .q-title{left:64px;font-size:40px;font-weight:400}

  .check{display:flex;align-items:flex-start;gap:24px;font-size:42px;line-height:48px}
  .check .box{width:40px;height:40px;border:3px solid #555;background:var(--white);margin-top:4px;flex:none}
  .check small{display:block;font-size:30px;line-height:36px}

  .map{left:48px;top:1680px;width:1104px;height:800px;background:linear-gradient(135deg,#f4f5f8 0%,#e8eaf2 100%)}
  .map-title{left:0;top:1700px;width:1200px;text-align:center;font-size:34px;letter-spacing:2px}

  .tag{height:92px;border-radius:46px;background:var(--tag);color:var(--white);font-family:"Noto Sans JP",sans-serif;font-size:32px;display:flex;align-items:center;justify-content:space-between;padding:0 40px 0 44px}
  .tag .x{font-size:40px}

  .select{top:2972px;height:80px;border:3px solid #999;border-radius:6px;background:var(--white);font-family:"Noto Sans JP",sans-serif;font-size:32px;display:flex;align-items:center;justify-content:space-between;padding:0 28px 0 44px}
  .unit{top:2990px;font-size:36px}

  .btn{top:4052px;width:380px;height:92px;background:var(--btn);border:3px solid var(--btn-border);font-family:"Noto Sans JP",sans-serif;font-size:32px;display:flex;align-items:center;justify-content:center}

  .site-footer{left:0;top:4232px;width:1200px;height:488px;background:linear-gradient(160deg,#2e2e8c 0%,var(--footer-blue) 55%,#4a4ab0 100%)}
  .page-top{right:64px;top:4290px;color:var(--white);font-family:"Noto Sans JP",sans-serif;font-size:34px;letter-spacing:2px}
  .copyright{left:0;top:4612px;width:1200px;text-align:center;color:var(--white);font-family:"Noto Sans JP",sans-serif;font-size:24px}
</style>
</head>
<body>

<header class="abs site-header">
  <h1 class="abs site-title">医療機関<br>海外渡航前ワクチン接種予約サイト</h1>
  <div class="abs menu-btn"><span class="bar"></span><span class="bar"></span><span class="bar"></span><span class="label">MENU</span></div>
</header>

<div class="abs step-bar"><p>渡航先・出発日・滞在期間</p></div>

<div class="abs hero" role="img" aria-label="スーツ姿のビジネスマンが電話をしている写真"></div>
<p class="abs hero-copy">Before traveling abroad<br>Vaccine reservation site</p>

<!-- 1 destination -->
<p class="abs q-title" style="top:1384px">1.渡航先を選択してください（複数指定可能）</p>
<div class="abs check" style="left:230px;top:1490px">
  <span class="box"><svg width="34" height="34" viewBox="0 0 34 34"><path d="M6 17 L14 25 L28 8" fill="none" stroke="#222" stroke-width="4"/></svg></span>
  <div>地図<small>から探す</small></div>
</div>
<div class="abs check" style="left:610px;top:1490px">
  <span class="box"></span>
  <div>キーワード<small>から探す</small></div>
</div>

<div class="abs map" role="img" aria-label="大陸ごとに色分けされた世界地図（SEVEN CONTINENTS）"></div>
<p class="abs map-title">SEVEN CONTINENTS</p>

<div class="abs tag" style="left:48px;top:2556px;width:540px">シドニー<span class="x">×</span></div>
<div class="abs tag" style="left:608px;top:2556px;width:544px">ニュージーランド<span class="x">×</span></div>
<div class="abs tag" style="left:48px;top:2684px;width:540px">オセアニア<span class="x">×</span></div>

<!-- 2 departure -->
<p class="abs q-title" style="top:2852px">2.出発日を選択してください。</p>
<div class="abs select" style="left:72px;width:280px">2021<svg width="28" height="18" viewBox="0 0 28 18"><path d="M3 3 L14 14 L25 3" fill="none" stroke="#222" stroke-width="4"/></svg></div>
<span class="abs unit" style="left:372px">年</span>
<div class="abs select" style="left:432px;width:280px">5<svg width="28" height="18" viewBox="0 0 28 18"><path d="M3 3 L14 14 L25 3" fill="none" stroke="#222" stroke-width="4"/></svg></div>
<span class="abs unit" style="left:732px">月</span>
<div class="abs select" style="left:780px;width:280px">21<svg width="28" height="18" viewBox="0 0 28 18"><path d="M3 3 L14 14 L25 3" fill="none" stroke="#222" stroke-width="4"/></svg></div>

<!-- 3 stay length -->
<p class="abs q-title" style="top:3212px">3.滞在期間を選択してください。</p>
<div class="abs check" style="left:230px;top:3330px">
  <span class="box"><svg width="34" height="34" viewBox="0 0 34 34"><path d="M6 17 L14 25 L28 8" fill="none" stroke="#222" stroke-width="4"/></svg></span>
  <div>1ヶ月未満</div>
</div>
<div class="abs check" style="left:610px;top:3330px">
  <span class="box"></span>
  <div>1ヶ月以上</div>
</div>

<!-- 4 purpose -->
<p class="abs q-title" style="top:3604px">4.渡航目的を選択してください。</p>
<div class="abs check" style="left:230px;top:3722px">
  <span class="box"><svg width="34" height="34" viewBox="0 0 34 34"><path d="M6 17 L14 25 L28 8" fill="none" stroke="#222" stroke-width="4"/></svg></span>
  <div>仕事</div>
</div>
<div class="abs check" style="left:610px;top:3722px">
  <span class="box"></span>
  <div>旅行</div>
</div>
<div class="abs check" style="left:230px;top:3860px">
  <span class="box"></span>
  <div>留学</div>
</div>
<div class="abs check" style="left:610px;top:3860px">
  <span class="box"></span>
  <div>その他</div>
</div>

<div class="abs btn" style="left:160px">簡易予約</div>
<div class="abs btn" style="left:580px">詳細予約</div>

<footer class="abs site-footer" role="img" aria-label="青く色調補正された医療現場の写真"></footer>
<p class="abs page-top">PAGE&nbsp;&nbsp;TOP ▲</p>
<p class="abs copyright">Copyright ©海外渡航前ワクチン接種予約サイト All Rights Reserved.</p>

</body>
</html>
```